Bakery Introducing a Crumbtastic Handcrafted Graham Cracker "Honey Crispets"

Though our Nibble On! brand name is well established, we're using our sister company's logo for this new product, as it fits better with the handcrafted artisan look we're going for. This "Marlow's Biscuits" logo is attached. The "Honey Crispets" are all natural, hand-crafted, and made with organic whole wheat flour. They will be packaged in two 6-packs in a stand-up, tin-tie top, resealable paper bag. Dimensions attached. The design needs to be 7 colors or less (including the logo), and either wrap around the entire bag, or be sectioned into panels. We'd like to emphasize the Honey Crispets all natural, butter-filled, deliciousness in a way that is warm, classic, and homey. Ideas & inspiration attached.
Updates

Target Market(s)

Shoppers at upscale grocery stores (Fresh Harvest, Larkspur Pantry, Verdant Provisions, etc.) who desire natural, local, handcrafted products.

Industry/Entity Type

It Company

Font styles to use
Serif
Decorative

Requirements
Must have
• Marlow's Biscuits Logo
• Honey Crispets
• Handcrafted
• All Natural
Nice to have
• Some way of emphasizing all the butter!
• Warm Colors
• A Vintage Feel

```html
<!DOCTYPE html>
<html lang="en">
<head>
<meta charset="utf-8">
<title>Honey Crispets – Bag Panels</title>
<link rel="stylesheet" href="https://fonts.googleapis.com/css2?family=Lobster&family=Dancing+Script:wght@500;700&family=Sansita:wght@800&family=Arimo:wght@400;700&family=Archivo+Narrow:wght@400;700&display=swap">
<style>
  :root{
    --yellow:#f8f08c;
    --yellow-soft:#f6ed9a;
    --cream:#fcf7dc;
    --gold:#d9bb5c;
    --gold-light:#e8d27a;
    --brown:#4a2a15;
    --rust:#b1420f;
    --ink:#3b2414;
    --cracker:#c9a55c;
    --cracker-dark:#a9833f;
    --label:#fffdf0;
  }
  *{box-sizing:border-box;margin:0;padding:0}
  html,body{width:1000px;height:1200px;overflow:hidden;background:#fff}
  body{font-family:"Arimo",Arial,sans-serif;color:var(--ink)}
  .canvas{position:relative;width:1000px;height:1200px}

  .panel{position:absolute;overflow:hidden}
  .row-classic .panel{top:12px;height:586px;background:var(--yellow)}
  .row-bright .panel{top:605px;height:587px;background:var(--cream)}
  .p-front{left:43px;width:255px}
  .p-side-a{left:305px;width:188px}
  .p-side-b{left:500px;width:190px}
  .p-back{left:697px;width:253px}

  .abs{position:absolute}
  .fill-svg{position:absolute;left:0;top:0;width:100%;height:100%}
  .front-frame{position:absolute;inset:7px;border:1px solid var(--gold);pointer-events:none}

  /* brand mark */
  .brand{position:absolute;display:flex;align-items:center;gap:5px;font-family:"Arimo",Arial,sans-serif;font-weight:700;color:var(--brown);white-space:nowrap}
  .brand-dot{border-radius:50%;background:var(--brown);flex:none}
  .brand-lg{font-size:13px}
  .brand-lg .brand-dot{width:34px;height:34px}
  .brand-sm{font-size:8px}
  .brand-sm .brand-dot{width:18px;height:18px}

  /* ribbons */
  .ribbon{position:absolute;display:flex;align-items:center;justify-content:center;text-align:center}
  .ribbon-script{font-family:"Dancing Script",cursive;font-weight:700;font-size:15px;color:var(--brown);background:var(--cream)}
  .ribbon-flour{font-size:8.5px;letter-spacing:.3px;color:#fff8dc;background:var(--gold)}
  .ribbon-bold{font-family:"Sansita",Georgia,serif;font-weight:800;font-size:14px;color:var(--rust);background:var(--yellow)}
  .flour-line{position:absolute;font-size:8.5px;letter-spacing:.3px;color:var(--ink);text-align:center}

  /* titles */
  .title-retro{position:absolute;left:0;width:100%;text-align:center;font-family:"Lobster",cursive;color:var(--brown);line-height:.95;font-size:46px}
  .title-script{position:absolute;left:0;width:100%;text-align:center;font-family:"Dancing Script",cursive;font-weight:500;color:var(--rust);line-height:1;font-size:40px}

  .placeholder{position:absolute}
  .photo-crackers{border-radius:8px;background:radial-gradient(circle at 45% 40%,#d7b06a,#b98a45 70%,#a57837)}
  .art-crackers{background:linear-gradient(135deg,var(--cracker),var(--cracker-dark))}
  .art-mini{background:linear-gradient(135deg,#d0ac62,#a9833f)}
  .art-plate{border-radius:50% 50% 45% 45%;background:linear-gradient(180deg,#f7e27a,#fffbe6)}

  /* info card */
  .info-card{position:absolute;border-radius:8px;padding:8px 10px}
  .info-card.classic{background:var(--cream)}
  .info-card.bright{background:#fff;border:1px solid var(--rust)}
  .info-card .brand{position:relative;justify-content:center;margin:6px 0 12px}
  .body-copy{font-size:8.5px;line-height:1.35;color:#1d140d}

  /* nutrition */
  .nutrition{position:absolute;background:var(--label);border:1.5px solid #111;padding:3px 4px;font-family:"Archivo Narrow",Arial,sans-serif;color:#111;font-size:7px;line-height:1.25}
  .nutrition h3{font-family:"Arimo",Arial,sans-serif;font-weight:700;font-size:15px;letter-spacing:-.4px;line-height:1}
  .nutrition .rule-thick{border-top:5px solid #111;margin:2px 0}
  .nutrition .rule-mid{border-top:2.5px solid #111;margin:1px 0}
  .nutrition .line{display:flex;justify-content:space-between;border-top:.5px solid #111;padding:1px 0}
  .nutrition .indent{padding-left:7px}
  .nutrition .right{text-align:right;font-size:5.5px;padding:1px 0}
  .nutrition .fine{font-size:5.5px;line-height:1.2;padding:2px 0}

  .caption{position:absolute;font-size:8px;line-height:1.3}
  .caption.on-dark{color:#f7e36a}
  .caption.on-light{color:#2a1a0e}
  .headline-retro{position:absolute;left:0;width:100%;text-align:center;font-family:"Lobster",cursive;font-size:40px;color:var(--brown)}
  .headline-script{position:absolute;left:0;width:100%;text-align:center;font-family:"Dancing Script",cursive;font-weight:500;font-size:38px;color:var(--rust)}
  .back-copy{position:absolute;left:20px;width:213px;text-align:center;font-size:10.5px;line-height:1.38}
  .back-copy.classic{color:#1d140d}
  .back-copy.bright{color:var(--rust)}
  .fine-print{position:absolute;left:10px;width:225px;font-size:6px;line-height:1.35}
  .fine-print.classic{color:#f3df6b}
  .fine-print.bright{color:#fff3d0}
</style>
</head>
<body>
<div class="canvas">

  <!-- ============ CLASSIC ROW ============ -->
  <section class="row-classic">

    <div class="panel p-front">
      <svg class="fill-svg" viewBox="0 0 255 586" preserveAspectRatio="none">
        <polygon points="0,472 255,460 255,470 0,482" fill="var(--gold)"/>
        <polygon points="0,490 255,478 255,488 0,500" fill="var(--gold)"/>
        <polygon points="0,508 255,496 255,506 0,518" fill="var(--gold)"/>
        <polygon points="0,526 255,514 255,586 0,586" fill="var(--brown)"/>
      </svg>
      <div class="front-frame"></div>
      <div class="brand brand-lg" style="left:50px;top:122px"><span class="brand-dot"></span>Marlow's Biscuits</div>
      <div class="ribbon ribbon-script" style="left:20px;top:180px;width:215px;height:32px">Handcrafted • All Natural</div>
      <div class="title-retro" style="top:232px">Honey<br>Crispets</div>
      <div class="placeholder art-mini" role="img" aria-label="Small illustration of two graham crackers" style="left:113px;top:318px;width:30px;height:36px"></div>
      <div class="ribbon ribbon-flour" style="left:16px;top:367px;width:223px;height:24px">MADE WITH ORGANIC WHOLE WHEAT FLOUR</div>
      <div class="placeholder photo-crackers" role="img" aria-label="Photo of a graham cracker close-up" style="left:39px;top:398px;width:180px;height:158px"></div>
    </div>

    <div class="panel p-side-a">
      <svg class="fill-svg" viewBox="0 0 188 586" preserveAspectRatio="none">
        <polygon points="0,455 188,440 188,450 0,465" fill="var(--gold)"/>
        <polygon points="0,474 188,459 188,469 0,484" fill="var(--gold)"/>
        <polygon points="0,493 188,478 188,488 0,503" fill="var(--gold)"/>
        <polygon points="0,520 188,500 188,586 0,586" fill="var(--brown)"/>
      </svg>
      <div class="placeholder art-crackers" role="img" aria-label="Illustration of two graham crackers, tilted" style="left:22px;top:122px;width:130px;height:165px"></div>
      <div class="info-card classic" style="left:15px;top:313px;width:158px;height:200px">
        <div class="brand brand-sm"><span class="brand-dot"></span>Marlow's Biscuits</div>
        <p class="body-copy">Lorem ipsum dolor sit amet, te has velit novum regione. Ne possit regione probatus est, ad sea integre virtute. Ei tibique corrumpit signife rumque per, iudico veniam legimus vis ea. Usu id detracto indoc tum, harum mucius Aconsequat an per. At quo purto omnes. Lorem regione probatus est, ad sea integre virtute. Ei tibique corrumpit signife rumque per, iudico veniam legimus.</p>
      </div>
    </div>

    <div class="panel p-side-b">
      <svg class="fill-svg" viewBox="0 0 190 586" preserveAspectRatio="none">
        <polygon points="0,410 190,425 190,437 0,422" fill="var(--gold)"/>
        <polygon points="0,432 190,447 190,459 0,444" fill="var(--gold)"/>
        <polygon points="0,454 190,469 190,481 0,466" fill="var(--gold)"/>
        <polygon points="0,476 190,491 190,503 0,488" fill="var(--gold)"/>
        <polygon points="0,515 190,512 190,586 0,586" fill="var(--brown)"/>
      </svg>
      <div class="nutrition" style="left:30px;top:142px;width:128px">
        <h3>Nutrition Facts</h3>
        <div>Serving Size 1 medium apple<br>(154g / 5.5 oz.)</div>
        <div class="rule-thick"></div>
        <div>Amount Per Serving</div>
        <div class="line"><span>Calories 80</span><span>Calories from Fat 0</span></div>
        <div class="rule-mid"></div>
        <div class="right">% Daily Value**</div>
        <div class="line"><span>Total Fat 0g</span><span>0%</span></div>
        <div class="line indent"><span>Saturated Fat 0g</span><span>0%</span></div>
        <div class="line indent"><span>Trans Fat 0g</span><span>0%</span></div>
        <div class="line"><span>Cholesterol 0mg</span><span>0%</span></div>
        <div class="line"><span>Sodium 0mg</span><span>0%</span></div>
        <div class="line"><span>Potassium 170mg</span><span>5%</span></div>
        <div class="line"><span>Total Carbohydrate 22g</span><span>7%</span></div>
        <div class="line indent"><span>Dietary Fiber 5g</span><span>20%</span></div>
        <div class="line indent"><span>Sugars 16g</span><span></span></div>
        <div class="line"><span>Protein 0g</span><span></span></div>
        <div class="rule-thick"></div>
        <div class="line" style="border:0"><span>Vitamin A 2% &nbsp;•</span><span>Vitamin C 8%</span></div>
        <div class="line"><span>Calcium 0% &nbsp;&nbsp;•</span><span>Iron 2%</span></div>
        <div class="fine" style="border-top:.5px solid #111">* Percent Daily Values are based on a 2,000 calorie diet. Your daily values may be higher or lower depending on your calorie needs.</div>
        <div class="fine" style="border-top:.5px solid #111">Calories per gram:<br>Fat 9 &nbsp;•&nbsp; Carbohydrate 4 &nbsp;•&nbsp; Protein 4</div>
      </div>
      <div class="placeholder art-mini" role="img" aria-label="Small illustration of two graham crackers" style="left:25px;top:522px;width:30px;height:36px"></div>
      <div class="caption on-dark" style="left:72px;top:538px">(Photo of actual crackers<br>package or crackers solo.)</div>
    </div>

    <div class="panel p-back">
      <svg class="fill-svg" viewBox="0 0 253 586" preserveAspectRatio="none">
        <polygon points="0,455 253,470 253,482 0,467" fill="var(--gold)"/>
        <polygon points="0,477 253,492 253,504 0,489" fill="var(--gold)"/>
        <polygon points="0,499 253,514 253,526 0,511" fill="var(--gold)"/>
        <polygon points="0,521 253,536 253,548 0,533" fill="var(--gold)"/>
        <polygon points="0,550 253,552 253,586 0,586" fill="var(--brown)"/>
      </svg>
      <div class="placeholder art-mini" role="img" aria-label="Illustration of graham crackers with a pat of butter on a plate" style="left:70px;top:132px;width:80px;height:50px"></div>
      <div class="caption on-light" style="left:126px;top:134px">(Photo of actual crackers<br>package or crackers solo.)</div>
      <div class="headline-retro" style="top:205px">Delicious!</div>
      <p class="back-copy classic" style="top:250px">Lorem ipsum dolor sit amet, te has velit novum regione. Ne possit regione probatus est, ad sea integre virtute. Ei tibique corrumpit signife rumque per, iudico veniam legimus vis ea. Usu id detracto indoc tum, harum mucius Aconsequat an per. At quo purto omnes. Lorem regione probatus est, ad sea integre virtute. Ei tibique corrumpit signife per, iudico veniam legimusprobatus est, ad sea integre virtute Ei tibique.</p>
      <p class="fine-print classic" style="top:554px">Tum, harum mucius Aconsequat an per. At quo purto omnes. Lorem regione probatus est, ad sea integre virtute. Ei tibique corrumpit signife per, iudico veniam legimusprobatus est, ad sea integre virtute Ei tibique.</p>
    </div>
  </section>

  <!-- ============ BRIGHT ROW ============ -->
  <section class="row-bright">

    <div class="panel p-front">
      <svg class="fill-svg" viewBox="0 0 255 587" preserveAspectRatio="none">
        <polygon points="0,0 255,0 255,36 247,44 239,36 231,44 223,36 215,44 207,36 199,44 191,36 183,44 175,36 167,44 159,36 151,44 143,36 135,44 127,36 119,44 111,36 103,44 95,36 87,44 79,36 71,44 63,36 55,44 47,36 39,44 31,36 23,44 15,36 7,44 0,36" fill="var(--yellow)"/>
        <rect x="0" y="430" width="255" height="9" fill="var(--yellow)"/>
        <rect x="0" y="447" width="255" height="9" fill="var(--yellow)"/>
        <rect x="0" y="464" width="255" height="9" fill="var(--yellow)"/>
        <rect x="0" y="487" width="255" height="100" fill="var(--rust)"/>
        <ellipse cx="127" cy="240" rx="108" ry="68" fill="var(--yellow)" stroke="var(--gold)" stroke-width="2"/>
        <ellipse cx="127" cy="240" rx="101" ry="61" fill="none" stroke="var(--rust)" stroke-width="1"/>
      </svg>
      <div class="front-frame"></div>
      <div class="brand brand-lg" style="left:50px;top:112px"><span class="brand-dot"></span>Marlow's Biscuits</div>
      <div class="placeholder art-plate" role="img" aria-label="Illustration of butter on a plate" style="left:98px;top:160px;width:60px;height:22px"></div>
      <div class="title-script" style="top:200px">Honey<br>Crispets</div>
      <div class="placeholder art-mini" role="img" aria-label="Small illustration of two graham crackers" style="left:105px;top:292px;width:44px;height:38px"></div>
      <div class="ribbon ribbon-bold" style="left:16px;top:348px;width:223px;height:26px">Handcrafted • All Natural</div>
      <div class="flour-line" style="left:0;width:255px;top:381px">MADE WITH ORGANIC WHOLE WHEAT FLOUR</div>
      <div class="placeholder photo-crackers" role="img" aria-label="Photo of a graham cracker close-up" style="left:39px;top:398px;width:180px;height:178px"></div>
    </div>

    <div class="panel p-side-a">
      <svg class="fill-svg" viewBox="0 0 188 587" preserveAspectRatio="none">
        <polygon points="0,0 188,0 188,36 180,44 172,36 164,44 156,36 148,44 140,36 132,44 124,36 116,44 108,36 100,44 92,36 84,44 76,36 68,44 60,36 52,44 44,36 36,44 28,36 20,44 12,36 4,44 0,40" fill="var(--yellow)"/>
        <rect x="0" y="416" width="188" height="9" fill="var(--yellow)"/>
        <rect x="0" y="433" width="188" height="9" fill="var(--yellow)"/>
        <rect x="0" y="450" width="188" height="9" fill="var(--yellow)"/>
        <rect x="0" y="485" width="188" height="102" fill="var(--rust)"/>
      </svg>
      <div class="placeholder art-crackers" role="img" aria-label="Illustration of two graham crackers, tilted" style="left:22px;top:118px;width:130px;height:165px"></div>
      <div class="info-card bright" style="left:15px;top:318px;width:158px;height:188px">
        <div class="brand brand-sm"><span class="brand-dot"></span>Marlow's Biscuits</div>
        <p class="body-copy">Lorem ipsum dolor sit amet, te has velit novum regione. Ne possit regione probatus est, ad sea integre virtute. Ei tibique corrumpit signife rumque per, iudico veniam legimus vis ea. Usu id detracto indoc tum, harum mucius Aconsequat an per. At quo purto omnes. Lorem regione probatus est, ad sea integre virtute. Ei tibique corrumpit signife rumque per, iudico veniam legimus.</p>
      </div>
    </div>

    <div class="panel p-side-b">
      <svg class="fill-svg" viewBox="0 0 190 587" preserveAspectRatio="none">
        <polygon points="0,0 190,0 190,36 182,44 174,36 166,44 158,36 150,44 142,36 134,44 126,36 118,44 110,36 102,44 94,36 86,44 78,36 70,44 62,36 54,44 46,36 38,44 30,36 22,44 14,36 6,44 0,38" fill="var(--yellow)"/>
        <rect x="0" y="426" width="190" height="9" fill="var(--yellow)"/>
        <rect x="0" y="443" width="190" height="9" fill="var(--yellow)"/>
        <rect x="0" y="460" width="190" height="9" fill="var(--yellow)"/>
        <rect x="0" y="485" width="190" height="102" fill="var(--rust)"/>
      </svg>
      <div class="nutrition" style="left:28px;top:122px;width:134px">
        <h3>Nutrition Facts</h3>
        <div>Serving Size 1 medium apple<br>(154g / 5.5 oz.)</div>
        <div class="rule-thick"></div>
        <div>Amount Per Serving</div>
        <div class="line"><span>Calories 80</span><span>Calories from Fat 0</span></div>
        <div class="rule-mid"></div>
        <div class="right">% Daily Value**</div>
        <div class="line"><span>Total Fat 0g</span><span>0%</span></div>
        <div class="line indent"><span>Saturated Fat 0g</span><span>0%</span></div>
        <div class="line indent"><span>Trans Fat 0g</span><span>0%</span></div>
        <div class="line"><span>Cholesterol 0mg</span><span>0%</span></div>
        <div class="line"><span>Sodium 0mg</span><span>0%</span></div>
        <div class="line"><span>Potassium 170mg</span><span>5%</span></div>
        <div class="line"><span>Total Carbohydrate 22g</span><span>7%</span></div>
        <div class="line indent"><span>Dietary Fiber 5g</span><span>20%</span></div>
        <div class="line indent"><span>Sugars 16g</span><span></span></div>
        <div class="line"><span>Protein 0g</span><span></span></div>
        <div class="rule-thick"></div>
        <div class="line" style="border:0"><span>Vitamin A 2% &nbsp;•</span><span>Vitamin C 8%</span></div>
        <div class="line"><span>Calcium 0% &nbsp;&nbsp;•</span><span>Iron 2%</span></div>
        <div class="fine" style="border-top:.5px solid #111">* Percent Daily Values are based on a 2,000 calorie diet. Your daily values may be higher or lower depending on your calorie needs.</div>
        <div class="fine" style="border-top:.5px solid #111">Calories per gram:<br>Fat 9 &nbsp;•&nbsp; Carbohydrate 4 &nbsp;•&nbsp; Protein 4</div>
      </div>
      <div class="placeholder art-mini" role="img" aria-label="Small illustration of two graham crackers" style="left:25px;top:520px;width:30px;height:40px"></div>
      <div class="caption on-dark" style="left:72px;top:535px">(Photo of actual crackers<br>package or crackers solo.)</div>
    </div>

    <div class="panel p-back">
      <svg class="fill-svg" viewBox="0 0 253 587" preserveAspectRatio="none">
        <polygon points="0,0 253,0 253,38 245,44 237,36 229,44 221,36 213,44 205,36 197,44 189,36 181,44 173,36 165,44 157,36 149,44 141,36 133,44 125,36 117,44 109,36 101,44 93,36 85,44 77,36 69,44 61,36 53,44 45,36 37,44 29,36 21,44 13,36 5,44 0,40" fill="var(--yellow)"/>
        <rect x="0" y="426" width="253" height="9" fill="var(--yellow)"/>
        <rect x="0" y="443" width="253" height="9" fill="var(--yellow)"/>
        <rect x="0" y="460" width="253" height="9" fill="var(--yellow)"/>
        <rect x="0" y="485" width="253" height="102" fill="var(--rust)"/>
      </svg>
      <div class="placeholder art-mini" role="img" aria-label="Illustration of graham crackers with a pat of butter on a plate" style="left:70px;top:110px;width:80px;height:50px"></div>
      <div class="caption on-light" style="left:126px;top:106px">(Photo of actual crackers<br>package or crackers solo.)</div>
      <div class="headline-script" style="top:172px">Delicious!</div>
      <p class="back-copy bright" style="top:218px">Lorem ipsum dolor sit amet, te has velit novum regione. Ne possit regione probatus est, ad sea integre virtute. Ei tibique corrumpit signife rumque per, iudico veniam legimus vis ea. Usu id detracto indoc tum, harum mucius Aconsequat an per. At quo purto omnes. Lorem regione probatus est, ad sea integre virtute. Ei tibique corrumpit signife per, iudico veniam legimusprobatus est, ad sea integre virtute Ei tibique.</p>
      <p class="fine-print bright" style="top:536px">Tum, harum mucius Aconsequat an per. At quo purto omnes. Lorem regione probatus est, ad sea integre virtute. Ei tibique corrumpit signife per, iudico veniam legimusprobatus est, ad sea integre virtute Ei tibique.</p>
    </div>
  </section>

</div>
</body>
</html>
```